Mellow Truffles. We need a website as delcious as our chocolate.

I need a website to promote our humble chocolate business. We our proud of are chocolate because we use only our favorite ingredients. We believe in originality and complete enjoyment of our chocolates. I am looking for a sleek and smooth website. I would like to see typical pages such as contact information and an intro. I would like to have a product page, which can be easily updated with photos of new chocolate. I would also like to see a page where we can educate customers about chocolate. This might be tricky but I would like our customers to leave the site knowing they are getting great chocolate! I have a logo and general color scheme, which I will try to upload somewhere. I looking for an original and exciting website.
Updates

Websites we like:

1. http://www.paul-van-orlen.example/ (looks really good)

2. http://www.tremilcocoa.example/

uploaded logo !

Target Market(s)

People who enjoy chocolate.

Industry/Entity Type

Business

Requirements
Must have
• User Friendly
Page were pictures of new chocolate can be easily updated.

Nice to have
• Calming and appetizing music
Section where recent tweets can show up on the site.

```html
<!DOCTYPE html>
<html lang="en">
<head>
<meta charset="utf-8">
<title>Mellow Truffles</title>
<link rel="stylesheet" href="https://fonts.googleapis.com/css2?family=Roboto+Condensed:ital,wght@0,400;0,700;1,700&family=Arimo:wght@400;700&display=swap">
<style>
  :root {
    --bg-deep: #1f120c;
    --bg-mid: #3b2419;
    --band-light: #a07656;
    --band-mid: #7b5237;
    --band-dark: #4a2c1c;
    --frame: #8a5a3c;
    --frame-light: #c9a083;
    --panel: #3a2218;
    --panel-edge: #2a170f;
    --content-bg: #956a52;
    --text-light: #f4ece4;
    --text-muted: #c4ad9d;
    --ink: #2b1a12;
    --logo-oval: #b07f69;
    --logo-frame: #6b4330;
    --accent-red: #c8372f;
  }
  * { box-sizing: border-box; margin: 0; padding: 0; }
  html, body { width: 1200px; height: 891px; overflow: hidden; }
  body {
    position: relative;
    background: linear-gradient(180deg, var(--bg-deep) 0%, var(--bg-mid) 55%, #4a2d20 100%);
    font-family: "Arimo", Arial, sans-serif;
    color: var(--text-light);
  }
  .page { position: absolute; left: 100px; top: 0; width: 1004px; height: 891px; }
  .topbar {
    position: absolute; left: 0; top: 0; width: 1004px; height: 62px;
    background: linear-gradient(180deg, #8b6650, #a07a60);
  }
  .call {
    position: absolute; left: 26px; top: 14px;
    font-family: "Roboto Condensed", sans-serif; font-weight: 700; font-size: 26px;
    color: var(--ink);
  }
  .call .number { color: #5a3a2a; }
  .social { position: absolute; right: 8px; top: 10px; display: flex; gap: 8px; }
  .social span {
    width: 37px; height: 37px; border-radius: 6px;
    background: linear-gradient(180deg, #c2702d, #7d3e16);
    border: 1px solid #4a2510;
  }
  .tab {
    position: absolute; top: 74px; width: 110px; height: 78px;
  }
  .tab.left { left: 0; }
  .tab.right { right: 0; }
  .navband {
    position: absolute; left: 90px; top: 60px; width: 1024px; height: 76px;
    background: linear-gradient(180deg, var(--band-light) 0%, var(--band-mid) 45%, var(--band-dark) 100%);
    border-top: 2px solid #6d4228; border-bottom: 3px solid #5a3420;
  }
  .nav {
    position: absolute; top: 81px;
    display: flex; gap: 8px;
    font-family: "Roboto Condensed", sans-serif; font-weight: 700; font-size: 19px;
    text-transform: uppercase; list-style: none;
  }
  .nav.left { left: 128px; }
  .nav.right { left: 770px; gap: 10px; }
  .nav li { padding: 7px 10px; color: var(--text-light); text-shadow: 0 1px 2px rgba(0,0,0,.6); }
  .nav li.active {
    background: linear-gradient(180deg, #5c4a2c, #2e2414);
    border: 1px solid #9d8455; border-radius: 2px;
  }
  .logo { position: absolute; left: 462px; top: 10px; width: 272px; height: 174px; }
  .logo-name {
    position: absolute; left: 462px; top: 78px; width: 272px; text-align: center;
    font-family: "Roboto Condensed", sans-serif; font-weight: 700; font-size: 27px;
    color: var(--ink);
  }
  .showcase {
    position: absolute; left: 0; top: 141px; width: 1004px; height: 382px;
    background: var(--frame);
  }
  .hero {
    position: absolute; left: 6px; top: 4px; width: 741px; height: 374px;
    border: 3px solid #e8dcd2; border-radius: 3px;
    background: radial-gradient(ellipse at 60% 30%, #8a5a45 0%, #4b2a1d 45%, #2c160d 100%);
  }
  .thumbs {
    position: absolute; left: 752px; top: 4px; width: 246px; height: 374px;
    background: #e3d6cc; border-radius: 3px; padding: 4px;
  }
  .thumb { width: 238px; height: 176px; border: 2px solid #1c0f09; }
  .thumb.brownie { background: radial-gradient(ellipse at 50% 40%, #7c5240, #3a1e13 70%); }
  .thumb.box { margin-top: 14px; height: 176px; background: radial-gradient(circle at 50% 50%, #8a5c40, #3b2015 75%); }
  .arrow {
    position: absolute; left: 111px; width: 26px; height: 26px; border-radius: 50%;
    background: #2c1b12; border: 2px solid #d8cbbf;
  }
  .arrow.down { top: 0; }
  .arrow.up { bottom: -4px; }
  .arrow svg { display: block; margin: 7px auto; }
  .content {
    position: absolute; left: 0; top: 533px; width: 1004px; height: 358px;
    background: var(--content-bg);
  }
  .content-inner {
    position: absolute; left: 6px; top: 8px; width: 992px; height: 295px;
    background: linear-gradient(180deg, #4a2c1f, var(--panel) 60%, var(--panel-edge));
  }
  .welcome { position: absolute; left: 15px; top: 16px; width: 670px; }
  .welcome h1 {
    font-family: "Roboto Condensed", sans-serif; font-weight: 700; font-size: 27px;
    text-transform: uppercase; padding-bottom: 8px;
    border-bottom: 1px solid #120905; box-shadow: 0 1px 0 #5e3d2d;
  }
  .welcome p {
    margin-top: 16px; font-size: 11.3px; line-height: 20.5px; color: var(--text-muted);
  }
  .welcome p + p { margin-top: 20px; }
  .quick {
    position: absolute; left: 703px; top: 17px; width: 272px; height: 210px;
    border: 2px solid #5d3a28;
    background: linear-gradient(180deg, #6a4534, #4a2c20 60%, #3e241a);
  }
  .quick h2 {
    height: 44px; padding: 8px 12px;
    background: linear-gradient(180deg, #8d644c, #5b3a29);
    margin-right: 20px;
    font-family: "Roboto Condensed", sans-serif; font-weight: 700; font-size: 25px;
    text-transform: uppercase; text-shadow: 0 2px 2px rgba(0,0,0,.6);
  }
  .quick .phone {
    position: absolute; left: 12px; top: 54px; display: flex; align-items: center; gap: 8px;
    font-family: "Arimo", sans-serif; font-weight: 700; font-size: 25px;
  }
  .quick .mail {
    position: absolute; left: 18px; top: 88px; display: flex; align-items: center; gap: 10px;
    font-weight: 700; font-size: 13px;
  }
  .quick .blurb {
    position: absolute; left: 16px; top: 114px; width: 140px;
    font-family: "Roboto Condensed", sans-serif; font-style: italic; font-weight: 700;
    font-size: 15px; line-height: 20px;
  }
  .quick .heart {
    position: absolute; left: 152px; top: 112px; width: 116px; height: 96px;
    background: radial-gradient(ellipse at 50% 30%, #a84236 0%, #4a2a22 40%, #1e100b 90%);
    border-radius: 50% 50% 45% 45%;
  }
  .copyright {
    position: absolute; left: 0; top: 322px; width: 1004px; text-align: center;
    font-size: 12px; color: var(--text-light);
  }
</style>
</head>
<body>
  <svg class="tab left" viewBox="0 0 110 78" aria-hidden="true">
    <polygon points="0,39 36,0 110,0 110,78 36,78" fill="#6b4a36"/>
    <polygon points="6,39 38,5 110,5 110,73 38,73" fill="#8b6a52"/>
  </svg>
  <svg class="tab right" viewBox="0 0 110 78" aria-hidden="true">
    <polygon points="110,39 74,0 0,0 0,78 74,78" fill="#6b4a36"/>
    <polygon points="104,39 72,5 0,5 0,73 72,73" fill="#8b6a52"/>
  </svg>

  <div class="page">
    <header class="topbar">
      <div class="call">Call To Order : <span class="number">555.014.2200</span></div>
      <div class="social" aria-label="Social links"><span></span><span></span><span></span></div>
    </header>
  </div>

  <div class="navband"></div>

  <div class="page">
    <ul class="nav left">
      <li class="active">Home</li><li>About Us</li><li>Products</li>
    </ul>
    <ul class="nav right">
      <li>Photo Gallery</li><li>Contact Us</li>
    </ul>

    <svg class="logo" viewBox="0 0 272 174" aria-hidden="true">
      <path d="M40,14 Q136,-6 232,14 L262,40 L262,134 L232,160 Q136,180 40,160 L10,134 L10,40 Z" fill="var(--logo-frame)" stroke="#4a2a1b" stroke-width="2"/>
      <ellipse cx="136" cy="87" rx="112" ry="66" fill="var(--logo-oval)" stroke="#5a3625" stroke-width="4"/>
    </svg>
    <div class="logo-name">Mellow Truffles</div>

    <section class="showcase">
      <div class="hero" role="img" aria-label="Stacked chocolate brownies on a wooden board with warm bokeh lights"></div>
      <div class="thumbs">
        <div class="thumb brownie" role="img" aria-label="Chocolate brownie close-up"></div>
        <div class="thumb box" role="img" aria-label="Assorted chocolates in paper cups"></div>
        <span class="arrow down"><svg width="10" height="8" viewBox="0 0 10 8"><polygon points="0,0 10,0 5,7" fill="#e8dcd2"/></svg></span>
        <span class="arrow up"><svg width="10" height="8" viewBox="0 0 10 8"><polygon points="0,8 10,8 5,1" fill="#e8dcd2"/></svg></span>
      </div>
    </section>

    <section class="content">
      <div class="content-inner">
        <article class="welcome">
          <h1>Welcome</h1>
          <p>Lorem Ipsum is simply dummy text of the printing and typesetting industry. Lorem Ipsum has been the industry's standard dummy text ever since the 1500s, when an unknown printer took a galley of type and scrambled it to make a type specimen book. It has survived not only five centuries, but also the leap into electronic typesetting, remaining essentially unchanged. It was popularised in the 1960s with the release of Letraset sheets containing Lorem Ipsum passages, and more recently with desktop publishing software like Aldus PageMaker including versions of Lorem Ipsum.</p>
          <p>Lorem Ipsum is simply dummy text of the printing and typesetting industry. Lorem Ipsum has been the industry's standard dummy text ever since the 1500s, when an unknown printer took a galley of type and scrambled it to make a type specimen book. It has survived not only five centuries, but also the leap into electronic typesetting, passages, and more recently with desktop publishing software like Aldus PageMaker including versions of Lorem Ipsum.</p>
        </article>

        <aside class="quick">
          <h2>Quick Contact</h2>
          <div class="phone">
            <svg width="28" height="22" viewBox="0 0 28 22" aria-hidden="true"><path d="M2,8 Q14,-2 26,8 L22,11 L19,7 Q14,5 9,7 L6,11 Z M8,10 H20 L24,20 H4 Z" fill="#fff"/></svg>
            555-014-7731
          </div>
          <div class="mail">
            <svg width="18" height="12" viewBox="0 0 18 12" aria-hidden="true"><rect x="0.5" y="0.5" width="17" height="11" fill="none" stroke="#fff"/><polyline points="1,1 9,7 17,1" fill="none" stroke="#fff"/></svg>
            manager@mellowtruffles.example
          </div>
          <p class="blurb">Lorem ipsum dolor sit is consectetur adipiscing Donec dignissim varius justo.</p>
          <div class="heart" role="img" aria-label="Heart-shaped chocolate with red glaze"></div>
        </aside>
      </div>
      <p class="copyright">Copyright © 2012-2013 mellowtruffles.example. All Rights Reserved.</p>
    </section>
  </div>
</body>
</html>
```